Photojournalism/photography business needs a simple, timeless & professional letterhead design

We need a letterhead design for photography/photojournalism business called 'plomk', no capitals.

The letterhead needs to be:
- simple
- professional
- timeless
- easy to read
- consists of at least 2 colors to make it stands out.

We do mainly editorial photography, photo articles for various publications, travel, businesses, as well as people such as family and kids.

The final design should communicate professionalism, easy identification, attention grabbing, even if it has to be found among a stack of various papers on the clients' desks.

Target Market(s)

Various publications.

Industry/Entity Type

Business

Requirements
Must have
• Please use the logo attached.

```html
<!DOCTYPE html>
<html lang="en">
<head>
<meta charset="utf-8">
<title>plomk letterhead</title>
<link href="https://fonts.googleapis.com/css2?family=Quicksand:wght@700&display=swap" rel="stylesheet">
<style>
  :root {
    --backdrop: #666666;
    --paper: #ffffff;
    --ink: #000000;
    --sky: #00a8e6;
    --red: #ec1c24;
    --orange: #f7941d;
    --lime: #8dc63f;
    --crimson: #be1e2d;
    --forest: #1b5e3b;
    --sun: #ffde17;
    --violet: #9b00ff;
  }
  html, body {
    margin: 0;
    width: 1200px;
    height: 1000px;
    overflow: hidden;
    background: var(--backdrop);
  }
  .letterhead {
    position: absolute;
    left: 255px;
    top: 20px;
    width: 681px;
    height: 964px;
    background: var(--paper);
    overflow: hidden;
  }
  .corner-pattern {
    position: absolute;
    left: 0;
    top: 0;
  }
  .header-rule {
    position: absolute;
    left: 0;
    top: 41px;
    width: 400px;
    height: 14px;
    background: var(--ink);
  }
  .brand {
    position: absolute;
    left: 392px;
    top: 28px;
    width: 270px;
    height: 130px;
    box-sizing: border-box;
    padding: 0 18px;
    background: var(--paper);
    border-radius: 18px;
    display: flex;
    align-items: center;
    justify-content: center;
    overflow: hidden;
  }
  .brand-name {
    font-family: "Quicksand", sans-serif;
    font-weight: 700;
    font-size: 76px;
    line-height: 1;
    letter-spacing: -1px;
    color: var(--ink);
    white-space: nowrap;
    padding-bottom: 10px;
  }
  .footer-band {
    position: absolute;
    left: 0;
    bottom: 0;
    width: 681px;
    height: 84px;
    background: linear-gradient(90deg,
      var(--sky), var(--red), var(--orange), var(--lime), var(--crimson),
      var(--forest), var(--sun), var(--sky), var(--violet), var(--sky),
      var(--red), var(--orange), var(--lime), var(--crimson), var(--forest),
      var(--sun), var(--sky), var(--violet));
  }
</style>
</head>
<body>
  <main class="letterhead">
    <svg class="corner-pattern" width="681" height="260" viewBox="0 0 681 260" role="img" aria-label="Decorative pattern of repeated multicolour brand name tiles fading down the top-right corner">
      <defs>
        <linearGradient id="corner-colours" x1="0" y1="0" x2="1" y2="0">
          <stop offset="0" stop-color="var(--sky)"/>
          <stop offset="0.2" stop-color="var(--red)"/>
          <stop offset="0.4" stop-color="var(--orange)"/>
          <stop offset="0.55" stop-color="var(--lime)"/>
          <stop offset="0.7" stop-color="var(--crimson)"/>
          <stop offset="0.85" stop-color="var(--forest)"/>
          <stop offset="1" stop-color="var(--sun)"/>
        </linearGradient>
        <linearGradient id="corner-fade" x1="0.3" y1="0" x2="0.6" y2="1">
          <stop offset="0" stop-color="#fff" stop-opacity="1"/>
          <stop offset="0.55" stop-color="#fff" stop-opacity="0.6"/>
          <stop offset="1" stop-color="#fff" stop-opacity="0"/>
        </linearGradient>
        <mask id="corner-mask">
          <rect width="681" height="260" fill="url(#corner-fade)"/>
        </mask>
      </defs>
      <polygon points="215,0 681,0 681,240 600,220 340,140 280,90" fill="url(#corner-colours)" mask="url(#corner-mask)"/>
    </svg>

    <div class="header-rule"></div>

    <div class="brand">
      <span class="brand-name">plomk</span>
    </div>

    <div class="footer-band" role="img" aria-label="Decorative band of repeated multicolour brand name tiles"></div>
  </main>
</body>
</html>
```